Hybrid Seed corn and Soybean Sales business needs a website.

We here at "KT Grain" feel that we need a website to show a very professional side to our customer base. Although no actual ordering will take place on this website, we would like to put Plot and field trail data on the website. Along with a brief page for each of our hybrids and a place for customers to sign up for a newsletter. The company we sell hybrids for is Morvanteld.com... Im not sure how this process works as far as myself updating the information or having the data actually put on the website, but feel free to contact me if you need the information. I will attach the logo for the company, (KT Grain).

Target Market(s)

Farmers, "Producers", Corn and soybean production

Industry/Entity Type

Business

Coding

Coded - Design and coding required

Number of Pages Required

5+ page

Colors
f78f20
ffffff

Requirements
Nice to have
• Similar layout to http://www.morvanteld.com/
• And it would be nice to incorporate our story into the website
• http://www.morvanteld.com/our-story/morvan-today/

```html
<!DOCTYPE html>
<html lang="en">
<head>
<meta charset="utf-8">
<title>KT Grain — Let's Grow Together</title>
<link href="https://fonts.googleapis.com/css2?family=Montserrat:wght@300;400;500;600;700&display=swap" rel="stylesheet">
<style>
  :root{
    --orange:#f78f20;
    --white:#ffffff;
    --ink:#3a3a3a;
    --muted:#555555;
    --card:#f6f6f6;
    --grey-btn:#c4c4c4;
    --footer:#4a4a4a;
    --footer-input:#2b2b2b;
    --nav-band:rgba(190,160,100,.35);
    --title-box:rgba(40,32,20,.78);
    --green:#3c9a35;
    --teal:#1c7f8f;
    --placeholder:#dfe3e7;
  }
  *{box-sizing:border-box;margin:0;padding:0}
  html,body{width:1023px;height:1200px;overflow:hidden}
  body{position:relative;background:var(--white);font-family:'Montserrat',sans-serif;color:var(--ink)}

  .hero{position:absolute;left:0;top:0;width:1023px;height:468px;
    background:linear-gradient(180deg,#f5e2b4 0%,#eecb7a 40%,#b58b45 70%,#6d6a35 100%);}
  .hero-rule{position:absolute;left:0;top:468px;width:1023px;height:3px;background:var(--orange)}

  .social{position:absolute;display:flex;gap:5px}
  .social span{width:25px;height:25px;border-radius:50%;background:#4b4b4b;display:block}
  .social .alt{background:#1da1e0}
  .header-social{left:138px;top:41px}

  .brand{position:absolute;left:0;width:1023px;top:36px;text-align:center;font-weight:700;font-size:30px;line-height:36px;color:var(--ink);letter-spacing:1px}
  .brand .dot{display:inline-block;width:18px;height:18px;background:var(--green);border-radius:50%;margin-right:9px;vertical-align:2px}

  .phone{position:absolute;right:137px;top:41px;display:flex;align-items:center;gap:8px;font-size:15px;font-weight:500;color:var(--ink)}
  .phone svg{width:25px;height:25px}

  .nav{position:absolute;left:0;top:106px;width:1023px;height:42px;background:var(--nav-band)}
  .nav ul{position:absolute;left:137px;top:0;list-style:none;display:flex;height:42px}
  .nav li{font-size:11.5px;font-weight:500;color:var(--ink);line-height:42px;letter-spacing:.3px}
  .nav .active{background:var(--orange);color:var(--white);font-weight:600;width:90px;text-align:center}
  .nav .i2{padding-left:21px}
  .nav .i3{padding-left:55px}
  .nav .i4{padding-left:55px}
  .nav .i5{padding-left:55px}
  .search{position:absolute;left:840px;top:0;width:46px;height:42px;background:rgba(170,140,90,.3);display:flex;align-items:center;justify-content:center}

  .tagline{position:absolute;left:310px;top:275px;width:427px;height:60px;background:var(--title-box);text-align:center}
  .tagline .bar{position:absolute;left:120px;top:0;width:102px;height:5px;background:var(--orange)}
  .tagline h1{font-size:28px;font-weight:700;color:var(--white);line-height:62px;letter-spacing:.5px}
  .tagline h1 em{font-style:normal;color:var(--orange)}
  .hero-sub{position:absolute;left:326px;top:338px;width:390px;text-align:center;color:var(--white);font-size:13px;font-weight:400;line-height:16.5px}

  .cards{position:absolute;left:137px;top:505px;display:flex;gap:13px}
  .card{position:relative;width:241px;height:284px;background:var(--card);text-align:center}
  .card .art{position:absolute;left:64px;top:26px;width:113px;height:64px;background:var(--placeholder)}
  .card h2{position:absolute;left:0;width:100%;top:104px;font-size:13px;font-weight:600;line-height:16px;color:var(--ink);letter-spacing:.3px}
  .card p{position:absolute;left:28px;width:185px;font-size:10px;line-height:12.6px;color:var(--muted)}
  .card .btn{position:absolute;left:51px;width:138px;height:31px;line-height:31px;font-size:11px;font-weight:600;color:var(--white);letter-spacing:.4px;background:var(--grey-btn);box-shadow:0 2px 0 #aaa}
  .card .btn.primary{background:var(--orange);box-shadow:none}

  .partners{position:absolute;left:137px;top:855px;width:749px;height:60px;display:flex;align-items:center;justify-content:space-between}
  .partner{font-size:24px;font-weight:700}
  .p1{color:#d8d0c6;font-weight:400}
  .p2{color:var(--teal)}
  .p3{color:#f2b8be}
  .p4{color:#c9c9c9}

  .footer{position:absolute;left:0;top:977px;width:1023px;height:223px;background:var(--footer);color:var(--white)}
  .f-brand{position:absolute;left:137px;top:45px;font-size:22px;font-weight:700;letter-spacing:1px}
  .f-brand .dot{display:inline-block;width:14px;height:14px;background:var(--green);border-radius:50%;margin-right:7px;vertical-align:1px}
  .copy{position:absolute;left:137px;top:106px;font-size:10.5px;font-weight:400}
  .footer-social{left:137px;top:131px}
  .footer-social span{background:#2f2f2f}
  .footer-social .alt{background:#1da1e0}
  .links{position:absolute;list-style:none;font-size:10.5px}
  .links li{height:22px}
  .links .current{color:var(--orange);font-weight:600}
  .col1{left:343px;top:48px}
  .col2{left:489px;top:48px}
  .news{position:absolute;left:643px;top:41px;width:243px}
  .news h3{font-size:13px;font-weight:600;letter-spacing:.3px}
  .news p{font-size:10.5px;margin-top:4px}
  .news .field{margin-top:11px;height:28px;background:var(--footer-input);border:1px solid #5c5c5c;font-size:8.5px;color:#8a8a8a;line-height:26px;padding-left:9px}
  .news .subscribe{margin-top:8px;margin-left:2px;width:76px;height:25px;line-height:25px;background:var(--orange);font-size:11px;font-weight:700;text-align:center}
</style>
</head>
<body>
  <div class="hero" role="img" aria-label="Photograph of a corn field at sunset"></div>
  <div class="hero-rule"></div>

  <div class="social header-social"><span></span><span class="alt"></span><span></span><span></span></div>
  <div class="brand"><span class="dot"></span>KT GRAIN</div>
  <div class="phone">+ 555 0142 738
    <svg viewBox="0 0 26 26"><circle cx="13" cy="13" r="11.5" fill="none" stroke="#f78f20" stroke-width="1.5"/><path d="M9 8c1-1 2 0 2.5 1.5s-.5 2-.5 2 1 2 3 3c0 0 .7-1 2-.5s2.5 1.5 1.5 2.5c-2 2-5 0-7-2.5S7 10 9 8z" fill="#f78f20"/></svg>
  </div>

  <nav class="nav">
    <ul>
      <li class="active">HOME</li>
      <li class="i2">OUR STORY</li>
      <li class="i3">PRODUCTS</li>
      <li class="i4">PLOT AND FIELD TRAIL</li>
      <li class="i5">CONTACT US</li>
    </ul>
    <div class="search"><svg width="12" height="12" viewBox="0 0 12 12"><circle cx="5" cy="5" r="3.8" fill="none" stroke="#444" stroke-width="1.3"/><path d="M8 8l3 3" stroke="#444" stroke-width="1.4"/></svg></div>
  </nav>

  <div class="tagline"><div class="bar"></div><h1>LET'S <em>GROW</em> TOGETHER</h1></div>
  <p class="hero-sub">Lorem ipsum dolor sit amet, consectetuer adipiscing elit, sed diam nonummy nibh euismod tincidunt ut laoreet dolore magna aliquam erat volutpat.</p>

  <section class="cards">
    <article class="card">
      <div class="art" role="img" aria-label="Illustration of a laptop showing field trial charts"></div>
      <h2>PLOT AND FIELD<br>TRAIL DATA</h2>
      <p style="top:142px">Ut wisi enim ad minim veniam, quis nostrud exerci tation ullamcorper suscipit lobortis nisl ut aliquip ex ea commodo consequat.</p>
      <div class="btn" style="top:224px">VIEW DATA</div>
    </article>
    <article class="card">
      <div class="art" role="img" aria-label="Illustration of a laptop showing the company name"></div>
      <h2>THE SEED YOU NEED</h2>
      <p style="top:142px">Duis autem vel eum iriure dolor in hendrerit in vulputate velit esse molestie consequat, vel illum dolore eu feugiat nulla facilisis at vero eros et accumsan et iusto odio dignissim feugait nulla facilisi.</p>
      <div class="btn primary" style="top:236px">SEE PRODUCTS</div>
    </article>
    <article class="card">
      <div class="art" role="img" aria-label="Illustration of a laptop showing a seedling"></div>
      <h2>OUR STORY</h2>
      <p style="top:142px">Vel illum dolore eu feugiat nulla facilisis at vero eros et accumsan et iusto odio dignissim qui blandit praesent luptatum zzril delenit augue duis dolore te feugait nulla facilisi.</p>
      <div class="btn" style="top:224px">READ MORE</div>
    </article>
  </section>

  <div class="partners">
    <span class="partner p1">Morvanteld</span>
    <span class="partner p2">Fieldwise</span>
    <span class="partner p3">BRENNOR</span>
    <span class="partner p4">Brennor Agri</span>
  </div>

  <footer class="footer">
    <div class="f-brand"><span class="dot"></span>KT GRAIN</div>
    <div class="copy">© 2015 KT GRAIN. All rights reserved.</div>
    <div class="social footer-social"><span></span><span class="alt"></span><span></span><span></span></div>
    <ul class="links col1">
      <li class="current">Home</li>
      <li>Products</li>
      <li>Our Story</li>
      <li>Plot and Feild Trail Data</li>
      <li>Contact Us</li>
    </ul>
    <ul class="links col2">
      <li>Privacy Statement</li>
      <li>Govt. Policies</li>
    </ul>
    <div class="news">
      <h3>NEWSLETTER SUBSCRIPTION</h3>
      <p>Subscribe to our newsletter stay connected!</p>
      <div class="field">YOUR EMAIL HERE &gt;&gt;&gt;</div>
      <div class="subscribe">SUBSCRIBE</div>
    </div>
  </footer>
</body>
</html>
```